Businees Trifold Makeover

Flyer will have rates and why use us
Pictures ….

Industry/Entity Type

tourism fishing charter

Requirements
Must have
• redo rates guest expeience to specializing in one and two person charters...

```html
<!DOCTYPE html>
<html lang="en">
<head>
<meta charset="utf-8">
<title>Tidewater Coast Charters – Trifold Brochure</title>
<link href="https://fonts.googleapis.com/css2?family=Montserrat:wght@400;600;700;800&family=Open+Sans:wght@400;600&display=swap" rel="stylesheet">
<style>
  :root{
    --navy:#1b2d78;
    --navy-deep:#141f5a;
    --teal:#2aa6c0;
    --teal-light:#6ccbdc;
    --sky:#bfe6ef;
    --white:#ffffff;
    --ink:#2b3350;
    --backdrop:#dcdcdc;
    --photo-water:#4d86a6;
    --photo-wood:#8f7658;
  }
  *{box-sizing:border-box;margin:0;padding:0}
  html,body{width:1200px;height:2400px;overflow:hidden;background:var(--backdrop)}
  body{font-family:"Open Sans",Arial,sans-serif;color:var(--ink);position:relative}
  .spread{position:absolute;left:60px;width:1080px;height:835px;display:flex;box-shadow:0 10px 30px rgba(0,0,0,.15);background:var(--white)}
  .spread--outside{top:250px}
  .spread--inside{top:1320px}
  .panel{position:relative;width:360px;height:835px;overflow:hidden}
  .photo{position:absolute;left:0;right:0}
  .wave{position:absolute;left:0;width:360px}
  h2,h3,.display{font-family:"Montserrat",Arial,sans-serif}
  .dots{display:flex;gap:5px;margin:6px 0 10px}
  .dots span{width:6px;height:6px;border-radius:50%;background:var(--teal-light)}
  .dots--center{justify-content:center}
  .brand{display:flex;align-items:center;gap:8px;font-family:"Montserrat",Arial,sans-serif;font-weight:700;color:var(--white)}
  .brand__dot{width:18px;height:18px;border-radius:50%;background:var(--white);flex:none}
  .url{font-family:"Montserrat",Arial,sans-serif;font-size:13px;color:var(--teal-light);letter-spacing:.3px}
  .phone-pill{display:inline-flex;align-items:center;gap:10px;background:var(--navy);color:var(--white);border-radius:20px;padding:5px 18px 5px 6px;font-family:"Montserrat",Arial,sans-serif;font-weight:700;font-size:22px}
  .phone-pill__icon{width:28px;height:28px;border-radius:50%;background:var(--teal);display:flex;align-items:center;justify-content:center}

  /* Outside: rates */
  .rates{background:var(--teal);color:var(--white)}
  .rates__body{position:absolute;top:26px;left:28px;right:28px;font-size:11.5px;line-height:1.5}
  .rates__title{font-size:19px;font-weight:800;letter-spacing:.5px}
  .rates__body p{margin-bottom:9px}
  .rates__body strong{font-family:"Montserrat",Arial,sans-serif;font-weight:700}
  .rates .brand{position:absolute;left:22px;top:705px;font-size:14px;z-index:2}

  /* Outside: booking */
  .booking__head{padding:28px 26px 0;text-align:center}
  .booking__title{color:var(--navy);font-size:22px;font-weight:800;line-height:1.2}
  .booking__text{font-size:11.5px;line-height:1.55;text-align:center;margin-bottom:14px}
  .booking__contact{text-align:center;margin-top:14px}
  .booking__name{font-family:"Montserrat",Arial,sans-serif;color:var(--navy);font-weight:800;font-size:16px;margin-bottom:4px}
  .booking__contact p{font-size:12px;line-height:1.55}
  .booking__photo{position:absolute;left:95px;top:480px;width:170px;height:170px;border-radius:50%;border:5px solid var(--white);background:radial-gradient(circle at 50% 40%,#8fc6de,#3f7fa6);z-index:2}
  .booking__foot{position:absolute;left:0;right:0;bottom:34px;text-align:center;z-index:2}
  .booking__cta{color:var(--white);font-size:21px;font-weight:800;line-height:1.2;margin-bottom:10px}

  /* Outside: cover */
  .cover .brand{position:absolute;left:32px;top:590px;font-size:17px;z-index:2}
  .cover__title{position:absolute;left:32px;right:16px;top:650px;color:var(--white);z-index:2;line-height:1.1}
  .cover__title .lead{font-weight:400;font-size:21px;letter-spacing:1px}
  .cover__title .strong{font-weight:800;font-size:26px;line-height:1.15;white-space:nowrap}
  .cover .url{position:absolute;left:32px;bottom:30px;z-index:2}

  /* Inside: left */
  .intro__text{position:absolute;top:320px;left:26px;right:26px}
  .section-title{color:var(--navy);font-size:17px;font-weight:800;line-height:1.2}
  .intro__text p,.call__text p{font-size:11.5px;line-height:1.55;margin-bottom:16px}
  .intro__foot{position:absolute;left:0;right:0;bottom:28px;text-align:center}
  .intro__foot .url{color:var(--navy);display:block;margin-top:8px}

  /* Inside: middle */
  .focus{background:var(--navy)}
  .focus__body{position:absolute;top:28px;left:26px;right:26px;color:var(--white);text-align:center}
  .focus__title{font-size:19px;font-weight:800;line-height:1.2}
  .focus__body p{font-size:11.5px;line-height:1.55;margin-bottom:12px;text-align:left}

  /* Inside: right */
  .call .brand{position:absolute;right:20px;top:20px;font-size:14px;z-index:2}
  .call__text{position:absolute;top:330px;left:26px;right:26px}
  .call__text .fine{font-size:10px;line-height:1.5;color:#5a6078}
</style>
</head>
<body>

<!-- Outside of the trifold -->
<section class="spread spread--outside">

  <article class="panel rates">
    <div class="rates__body">
      <h2 class="rates__title">CHARTER RATES</h2>
      <div class="dots"><span></span><span></span><span></span></div>
      <p>Unlock your next adventure with Tidewater Coast Charters. Our fishing charters are designed for one or two guests, giving you personal attention, expert guidance and plenty of time on the water.</p>
      <p><strong>4 HOUR CHARTER:</strong> Perfect for a morning or afternoon on the water, ideal for first-timers chasing salmon close to town.</p>
      <p><strong>6 HOUR CHARTER:</strong> More time to explore outer waters and target a wider range of species with your guide.</p>
      <p><strong>8 HOUR CHARTER:</strong> Our ultimate full-day trip, reaching the best grounds for salmon, halibut and lingcod with room to roam.</p>
      <p>Unforgettable fishing and wildlife await. Every charter includes tackle, bait, safety gear and fish cleaning, and licences can be arranged before departure.</p>
      <p>Call or email today to reserve your date; summer spots fill quickly, so book early and get ready for the trip of a lifetime.</p>
    </div>
    <div class="photo" role="img" aria-label="Photo of the charter boat moored at the marina" style="top:560px;height:170px;background:linear-gradient(160deg,#9fc7d8,#4f87a4 55%,#2f5e7c)"></div>
    <svg class="wave" style="top:650px" width="360" height="185" viewBox="0 0 360 185" aria-hidden="true">
      <path d="M0 40 C120 20 240 55 360 30 L360 60 C240 85 120 50 0 70Z" fill="var(--teal-light)"/>
      <path d="M0 60 C120 40 240 75 360 50 L360 185 L0 185Z" fill="var(--navy)"/>
    </svg>
    <div class="brand"><span class="brand__dot"></span>Tidewater Coast Charters</div>
  </article>

  <article class="panel booking">
    <div class="booking__head">
      <h2 class="booking__title">BOOK YOUR THRILLING CHARTER TODAY!</h2>
      <div class="dots dots--center"><span></span><span></span><span></span></div>
      <p class="booking__text">Your heart-pounding West Coast adventure is just a call away. Grab your phone and dial us, or email our team to book your spot. Tidewater Coast Charters is ready to make your fishing dreams come true with an exhilarating experience.</p>
      <span class="phone-pill">
        <span class="phone-pill__icon">
          <svg width="16" height="16" viewBox="0 0 24 24" aria-hidden="true"><path d="M6.6 10.8a15.1 15.1 0 0 0 6.6 6.6l2.2-2.2a1 1 0 0 1 1-.25 11.4 11.4 0 0 0 3.6.6 1 1 0 0 1 1 1V20a1 1 0 0 1-1 1A17 17 0 0 1 3 4a1 1 0 0 1 1-1h3.5a1 1 0 0 1 1 1c0 1.25.2 2.45.6 3.6a1 1 0 0 1-.25 1Z" fill="#fff"/></svg>
        </span>250-555-0147</span>
      <div class="booking__contact">
        <h3 class="booking__name">TIDEWATER COAST CHARTERS</h3>
        <p>Harbour Point, BC</p>
        <p>250-555-0147 | 250-555-0192</p>
        <p>hello@tidewatercoastcharters.com</p>
      </div>
    </div>
    <svg class="wave" style="top:560px" width="360" height="275" viewBox="0 0 360 275" aria-hidden="true">
      <path d="M0 40 C100 80 260 20 360 50 L360 275 L0 275Z" fill="var(--navy)"/>
      <path d="M0 30 C100 70 260 10 360 40 L360 50 C260 20 100 80 0 40Z" fill="var(--teal)"/>
    </svg>
    <div class="booking__photo" role="img" aria-label="Photo of a guest reeling in a fish on the water"></div>
    <div class="booking__foot">
      <h2 class="booking__cta">BOOK YOUR<br>CHARTER TODAY!</h2>
      <span class="url">www.tidewatercoastcharters.com</span>
    </div>
  </article>

  <article class="panel cover">
    <div class="photo" role="img" aria-label="Photo of a smiling angler on the dock holding a large salmon and lingcod" style="top:0;height:600px;background:linear-gradient(180deg,#7fae7a 0%,#5d8fa5 35%,var(--photo-water) 60%,var(--photo-wood) 100%)"></div>
    <svg class="wave" style="top:480px" width="360" height="355" viewBox="0 0 360 355" aria-hidden="true">
      <path d="M0 110 C120 80 250 40 360 0 L360 30 C250 70 120 110 0 140Z" fill="var(--teal-light)"/>
      <path d="M0 140 C120 110 250 70 360 30 L360 60 C250 100 120 140 0 165Z" fill="var(--teal)"/>
      <path d="M0 165 C120 140 250 100 360 60 L360 355 L0 355Z" fill="var(--navy)"/>
    </svg>
    <div class="brand"><span class="brand__dot"></span>Tidewater Coast Charters</div>
    <h1 class="cover__title display">
      <span class="lead">DISCOVER YOUR</span><br>
      <span class="strong">THRILLING WEST<br>COAST ADVENTURE</span>
    </h1>
    <span class="url">www.tidewatercoastcharters.com</span>
  </article>
</section>

<!-- Inside of the trifold -->
<section class="spread spread--inside">

  <article class="panel intro">
    <div class="photo" role="img" aria-label="Photo of the charter boat tied up at the marina dock" style="top:0;height:270px;background:linear-gradient(180deg,#a9cde0 0%,#d9e6ec 45%,#5f8fa8 100%)"></div>
    <svg class="wave" style="top:235px" width="360" height="70" viewBox="0 0 360 70" aria-hidden="true">
      <path d="M0 20 C120 0 240 40 360 15 L360 40 C240 65 120 25 0 45Z" fill="var(--navy)"/>
      <path d="M0 45 C120 25 240 65 360 40 L360 50 C240 75 120 35 0 55Z" fill="var(--teal)"/>
    </svg>
    <div class="intro__text">
      <h2 class="section-title">EXPERIENCE THE ULTIMATE WEST COAST ADVENTURE:</h2>
      <div class="dots"><span></span><span></span><span></span></div>
      <p>Welcome aboard the 25-foot Cruiser charter boat, where Tidewater Coast Charters and the legendary local guides are ready to take you on an unforgettable journey through the untamed beauty of the coast. Brace yourself for an adrenaline-pumping fishing and wildlife tour like no other!</p>
      <h2 class="section-title">AWE-INSPIRING WILDLIFE MOMENTS:</h2>
      <div class="dots"><span></span><span></span><span></span></div>
      <p>Venture into the heart of the wilderness, where coastal bears fish for salmon, showcasing their incredible hunting skills. Look up to the sky as bald eagles soar with breathtaking elegance overhead. These captivating wildlife moments are sure to leave you speechless.</p>
    </div>
    <div class="intro__foot">
      <span class="phone-pill">
        <span class="phone-pill__icon">
          <svg width="16" height="16" viewBox="0 0 24 24" aria-hidden="true"><path d="M6.6 10.8a15.1 15.1 0 0 0 6.6 6.6l2.2-2.2a1 1 0 0 1 1-.25 11.4 11.4 0 0 0 3.6.6 1 1 0 0 1 1 1V20a1 1 0 0 1-1 1A17 17 0 0 1 3 4a1 1 0 0 1 1-1h3.5a1 1 0 0 1 1 1c0 1.25.2 2.45.6 3.6a1 1 0 0 1-.25 1Z" fill="#fff"/></svg>
        </span>250-555-0147</span>
      <span class="url">www.tidewatercoastcharters.com</span>
    </div>
  </article>

  <article class="panel focus">
    <div class="focus__body">
      <h2 class="focus__title">ONE AND TWO PERSON<br>FISHING FOCUSSED</h2>
      <div class="dots dots--center"><span></span><span></span><span></span></div>
      <p>At Tidewater Coast Charters, we specialize in small, personal trips for one or two guests. With the whole boat and guide devoted to you, every hour is spent learning, casting and landing fish rather than waiting your turn. We tailor each outing to your skill level, goals and pace, so beginners and seasoned anglers alike feel right at home on board.</p>
      <p>For couples, friends or solo travellers, a private charter means flexible timing, quiet water and the freedom to chase the bite wherever it leads. Your guide shares local knowledge, rigging tips and stories from years on these waters.</p>
      <p>Throughout the journey, our guide will capture your proudest catches and the wild moments in between, so you leave with memories and photos worth sharing for years to come.</p>
    </div>
    <div class="photo" role="img" aria-label="Photo of a guest holding a freshly caught salmon beside the boat" style="top:560px;height:275px;background:linear-gradient(180deg,#6fa3bf,#3e6f8e 70%,#2a4f6a)"></div>
    <svg class="wave" style="top:535px" width="360" height="60" viewBox="0 0 360 60" aria-hidden="true">
      <path d="M0 0 L360 0 L360 20 C240 50 120 10 0 35Z" fill="var(--navy)"/>
      <path d="M0 35 C120 10 240 50 360 20 L360 30 C240 60 120 20 0 45Z" fill="var(--teal)"/>
    </svg>
  </article>

  <article class="panel call">
    <div class="photo" role="img" aria-label="Photo of the guide and a guest fishing from the back deck" style="top:0;height:290px;background:linear-gradient(180deg,#89b6cf 0%,#4e86a6 50%,#d7dde2 100%)"></div>
    <svg class="wave" style="top:250px" width="360" height="70" viewBox="0 0 360 70" aria-hidden="true">
      <path d="M0 20 C120 45 240 0 360 25 L360 45 C240 20 120 65 0 40Z" fill="var(--navy)"/>
      <path d="M0 40 C120 65 240 20 360 45 L360 55 C240 30 120 75 0 50Z" fill="var(--teal)"/>
    </svg>
    <div class="brand"><span class="brand__dot"></span>Tidewater Coast Charters</div>
    <div class="call__text">
      <h2 class="section-title">ANSWER THE CALL<br>OF THE WILD:</h2>
      <div class="dots"><span></span><span></span><span></span></div>
      <p>With our one and two-guest fishing charters, you can be assured of personal attention and a relaxing focus on your experience. Our guides take care of all the logistics, so you can relax and savour every moment of the adventure.</p>
      <h2 class="section-title">YOUR ADVENTURE AWAITS WITH TIDEWATER COAST CHARTERS</h2>
      <div class="dots"><span></span><span></span><span></span></div>
      <p>The 25-foot Cruiser Charter Boat: step aboard the sturdy, well-equipped vessel, renowned for its reliability and performance on the water. Its spacious deck ensures a comfortable and enjoyable ride while you take in the coastal scenery.</p>
      <p class="fine">Our licensed and insured guides hold current safety certifications. All gear is supplied and maintained, and every trip follows local fishing regulations to protect the waters we love.</p>
    </div>
  </article>
</section>

</body>
</html>
```